Marrowdale Institute Word Document Template

At the Marrowdale Institute, we want to offer our employees the ability to download branded word document templates that allow non-designers to create professional and on-brand documents. Through the use of theme preferences, locked elements and paragraph styles, the final deliverables should contain the brand elements identified at brand.mrwdl.edu including the primary logo, fonts, and colors.

GENERAL TEMPLATE
A multi-functional document that contains a range of styles and brand elements that can be used broadly. The template should be flexible enough to work as a single-page document, or a multi-page document.

Target Market(s)

Administrative staff and faculty (Non-designers) who create documents largely for internal use

Font styles to use
Sans Serif
Other font styles liked:
• Fonts are attached – Roboto should be used predominantly with Antonio and Zilla available to use when appropriate. Fonts should default to Arial if fonts are not installed.

Colors
fbed22
ffffff
000000

Requirements
Must have
• REQUIREMENTS:
Use brand assets at brand.mrwdl.edu (primary logo, fonts, colors are all available to download there).
If possible, fonts should default to Arial – if user does not have fonts installed.
Browse brand.mrwdl.edu to get a sense of the established look and feel.
No elements should bleed off the page.
The final deliverable should be as locked down as possible. The logo should not be editable.

ELEMENTS TO INCLUDE:
Masthead to include: Primary logo and Placeholder for Unit name
Paragraph styles:
Document Title
Subhead 1
Subhead 2
Body
Bullets
Photo Placeholder
Pull Quote
Caption
Footer to include statement (small): The Marrowdale Institute prohibits discrimination in employment, educational programs, and activities on the basis of race, creed, color, religion, national origin, age, sex, pregnancy, disability, genetic information, status as a U.S. veteran, service in the U.S. military, sexual orientation, gender identity, associational preferences, or any other classification that deprives the person of consideration as an individual. The university also affirms its commitment to providing equal opportunities and equal access to university facilities. For additional information on nondiscrimination policies, contact the Director, Bureau of Fair Access and Inclusion, the Marrowdale Institute, 418 Penwick Hall, Iowa City, IA 52279-4083, 319-482-6613 (voice), 319-482-6671 (TDD), inclusion@mrwdl.edu.
Nice to have
• Additional page templates for added flexibility would be nice...Such as a Cover sheet and/or Table of contents.

```html
<!DOCTYPE html>
<html lang="en">
<head>
<meta charset="utf-8">
<title>Marrowdale Institute Document Template</title>
<link rel="stylesheet" href="https://fonts.googleapis.com/css2?family=Antonio:wght@700&family=Roboto:ital,wght@0,400;0,500;0,700;0,900;1,400&display=swap">
<style>
  :root {
    --gold: #fbd400;
    --gold-line: #f5d21c;
    --black: #000000;
    --white: #ffffff;
    --ink: #1a1a1a;
    --muted: #555555;
    --stage: #e6e6e6;
    --rule: #9a9a9a;
    --cell: #f0f0f0;
    --placeholder: #e6edf8;
    --sky-top: #2f6fc4;
    --sky-mid: #8fb8e6;
    --lawn: #4f9a2c;
    --trees: #2d5a1e;
  }
  * { box-sizing: border-box; margin: 0; padding: 0; }
  html, body { width: 1200px; height: 3000px; overflow: hidden; }
  body { background: var(--stage); font-family: "Roboto", Arial, sans-serif; color: var(--ink); position: relative; }

  .page { position: absolute; width: 506px; height: 655px; background: var(--white); box-shadow: 0 2px 10px rgba(0,0,0,0.12); overflow: hidden; }
  .page--cover-alt { left: 614px; top: 452px; }
  .page--cover { left: 58px; top: 738px; }
  .page--styles { left: 58px; top: 1438px; }
  .page--lists { left: 614px; top: 1151px; }
  .page--contents { left: 614px; top: 1860px; }

  .cover-photo { position: absolute; left: 16px; top: 16px; width: 474px; height: 414px; }
  .cover-photo--columns { background: linear-gradient(180deg, var(--sky-top) 0%, var(--sky-mid) 35%, #d8dde2 55%, var(--trees) 72%, var(--lawn) 82%, #5fae34 100%); }
  .cover-photo--dome { background: linear-gradient(180deg, #3a7fd0 0%, #9ec4ea 30%, var(--trees) 45%, #1f4417 70%, var(--lawn) 82%, #65b53a 100%); }
  .cover-band { position: absolute; left: 16px; top: 430px; width: 474px; height: 207px; background: var(--gold); }

  .wordmark { font-family: "Antonio", Arial, sans-serif; font-weight: 700; color: var(--black); letter-spacing: 0.5px; line-height: 1; }
  .cover-alt-mark { position: absolute; left: 50px; top: 92px; font-size: 26px; }
  .cover-alt-divider { position: absolute; left: 203px; top: 72px; width: 2px; height: 68px; background: var(--black); }
  .cover-alt-text { position: absolute; left: 247px; top: 78px; width: 192px; font-size: 9.6px; line-height: 11.6px; }

  .cover-title { position: absolute; left: 36px; top: 14px; font-family: "Antonio", Arial, sans-serif; font-weight: 700; font-size: 50px; line-height: 1; letter-spacing: 0.5px; }
  .cover-lede { position: absolute; left: 38px; top: 74px; width: 402px; font-size: 11.5px; line-height: 13px; }
  .cover-unit { position: absolute; left: 40px; top: 170px; font-size: 9px; letter-spacing: 0.2px; }
  .cover-mark { position: absolute; right: 24px; top: 160px; font-size: 31px; }

  .masthead-unit { position: absolute; left: 41px; top: 27px; font-size: 8px; }
  .masthead-mark { position: absolute; right: 39px; top: 24px; font-size: 14px; color: var(--gold); }

  .doc-footer { position: absolute; left: 37px; top: 600px; width: 432px; border-top: 2px solid var(--gold-line); }
  .doc-footer p { width: 864px; padding-top: 8px; font-size: 8.4px; line-height: 10.4px; color: var(--muted); text-align: justify; transform: scale(0.5); transform-origin: 0 0; }

  .content { position: absolute; left: 41px; right: 41px; top: 60px; }
  .title-style { font-weight: 900; font-size: 28px; line-height: 32px; letter-spacing: 0.3px; margin-bottom: 10px; }
  .body-copy { font-size: 8.4px; line-height: 11.2px; margin-bottom: 5px; }
  .justify { text-align: justify; }
  .subhead-1 { font-weight: 700; font-size: 15px; line-height: 18px; margin: 12px 0 7px; }
  .subhead-2 { font-weight: 700; font-size: 11.5px; line-height: 14px; margin: 14px 0 5px; }
  .narrow { width: 268px; }
  .photo-placeholder { position: absolute; left: 316px; top: 277px; width: 149px; height: 149px; background: var(--placeholder); }
  .special-title { display: block; width: 268px; background: var(--gold); font-size: 10px; line-height: 13px; margin: 12px 0 5px; }

  .section-title { font-weight: 700; font-size: 16px; line-height: 20px; margin-bottom: 6px; }
  .bullets { list-style: none; font-size: 8px; }
  .bullets li { display: flex; align-items: center; height: 17.4px; }
  .bullets li.sub { padding-left: 29px; }
  .bullets svg { margin-right: 7px; flex: none; }
  .bullets li.sub svg { margin-right: 10px; }

  .data-table { border-collapse: collapse; font-size: 7.5px; }
  .data-table th { text-align: left; font-weight: 700; padding: 0 5px; height: 20px; }
  .data-table td { padding: 0 5px; height: 20.6px; }
  .table-gold { width: 423px; margin-top: 10px; }
  .table-gold th { background: var(--gold); }
  .table-gold td { border-bottom: 1px solid var(--rule); }
  .table-gold tr:nth-child(odd) td { background: #f6f6f6; }
  .table-black { width: 338px; margin-top: 6px; }
  .table-black th { background: var(--black); color: var(--white); border-right: 1px solid #666; }
  .table-black td { background: var(--cell); border: 1px solid #d6d6d6; }
  .table-black td:first-child { font-weight: 700; }
  .caption { font-style: italic; font-size: 7.5px; margin: 5px 0 10px; }
  .table-title-2 { font-weight: 400; font-size: 12.5px; line-height: 15px; }

  .pull-quote { position: absolute; left: 162px; top: 485px; width: 160px; }
  .pull-quote-mark { position: absolute; left: -22px; top: -6px; font-weight: 900; font-size: 30px; line-height: 1; color: var(--gold); }
  .pull-quote p { font-style: italic; font-size: 9px; line-height: 11.4px; }

  .contents-title { font-weight: 900; font-size: 23px; line-height: 28px; color: var(--gold); margin-bottom: 8px; }
  .toc { list-style: none; font-size: 8.4px; }
  .toc li { display: flex; align-items: baseline; height: 16.3px; font-weight: 500; color: #444; }
  .toc li.primary { color: var(--gold); font-weight: 700; }
  .toc .leader { flex: 1; border-bottom: 1px dotted currentColor; margin: 0 2px; transform: translateY(-2px); }
</style>
</head>
<body>

<section class="page page--cover-alt">
  <div class="cover-photo cover-photo--dome" role="img" aria-label="Campus lawn with trees and a golden-domed building under a blue sky"></div>
  <div class="cover-band">
    <div class="wordmark cover-alt-mark">MARROWDALE</div>
    <div class="cover-alt-divider"></div>
    <p class="cover-alt-text">Lorem ipsum dolor sit amet, consectetuer adipiscing elit, sed diam nonummy nibh euismod tincidunt ut laoreet dolore magna aliquam erat volutpat. Ut wisi enim ad minim veniam, quis nostrud exerci tation</p>
  </div>
</section>

<section class="page page--cover">
  <div class="cover-photo cover-photo--columns" role="img" aria-label="Stone columns on a lawn before a domed campus building under a cloudy sky"></div>
  <div class="cover-band">
    <h1 class="cover-title">DOCUMENT TITLE HERE</h1>
    <p class="cover-lede">Lorem ipsum dolor sit amet, consectetuer adipiscing elit, sed diam nonummy nibh euismod tincidunt ut laoreet dolore magna aliquam erat volutpat. Ut wisi enim ad minim veniam, quis nostrud exerci tation ullamcorper suscipit lobortis nisl ut aliquip ex ea commodo consequat. Duis autem vel eum iriure dolor in</p>
    <div class="cover-unit">DEPARTMENT NAME</div>
    <div class="wordmark cover-mark">MARROWDALE</div>
  </div>
</section>

<section class="page page--styles">
  <div class="masthead-unit">Document Title</div>
  <div class="wordmark masthead-mark">MARROWDALE</div>
  <div class="photo-placeholder" role="img" aria-label="Photo placeholder"></div>
  <div class="content">
    <h2 class="title-style">TITLE STYLE</h2>
    <p class="body-copy">Lorem ipsum dolor sit amet, consectetuer adipiscing elit. Maecenas porttitor congue massa. Fusce posuere, magna sed pulvinar ultricies, purus lectus malesuada libero, sit amet commodo magna eros quis urna.</p>
    <p class="body-copy">Nunc viverra imperdiet enim. Fusce est. Vivamus a tellus.</p>
    <p class="body-copy">Pellentesque habitant morbi tristique senectus et netus et malesuada fames ac turpis egestas. Proin pharetra nonummy pede. Mauris et orci.</p>
    <h3 class="subhead-1">HEADING 01</h3>
    <p class="body-copy">Lorem ipsum dolor sit amet, consectetuer adipiscing elit. Maecenas porttitor congue massa. Fusce posuere, magna sed pulvinar ultricies, purus lectus malesuada libero, sit amet commodo magna eros quis urna.</p>
    <p class="body-copy">Nunc viverra imperdiet enim. Fusce est. Vivamus a tellus.</p>
    <p class="body-copy">Pellentesque habitant morbi tristique senectus et netus et malesuada fames ac turpis egestas. Proin pharetra nonummy pede. Mauris et orci.</p>
    <h4 class="subhead-2">HEADING 02</h4>
    <p class="body-copy narrow justify">Lorem ipsum dolor sit amet, consectetuer adipiscing elit. Maecenas porttitor congue massa. Fusce posuere, magna sed pulvinar ultricies, purus lectus malesuada libero, sit amet commodo magna eros quis urna.</p>
    <p class="body-copy narrow">Nunc viverra imperdiet enim. Fusce est. Vivamus a tellus.</p>
    <p class="body-copy narrow">Pellentesque habitant morbi tristique senectus et netus et malesuada fames ac turpis egestas. Proin pharetra nonummy pede. Mauris et orci.</p>
    <span class="special-title">SPECIAL TITLE</span>
    <p class="body-copy justify">Lorem ipsum dolor sit amet, consectetuer adipiscing elit. Maecenas porttitor congue massa. Fusce posuere, magna sed pulvinar ultricies, purus lectus malesuada libero, sit amet commodo magna eros quis urna.</p>
    <p class="body-copy">Nunc viverra imperdiet enim. Fusce est. Vivamus a tellus.</p>
    <p class="body-copy">Pellentesque habitant morbi tristique senectus et netus et malesuada fames ac turpis egestas. Proin pharetra nonummy pede. Mauris et orci.</p>
  </div>
  <div class="doc-footer"><p>The Marrowdale Institute prohibits discrimination in employment, educational programs, and activities on the basis of race, creed, color, religion, national origin, age, sex, pregnancy, disability, genetic information, status as a U.S. veteran, service in the U.S. military, sexual orientation, gender identity, associational preferences, or any other classification that deprives the person of consideration as an individual. The university also affirms its commitment to providing equal opportunities and equal access to university facilities. For additional information on nondiscrimination policies, contact the Director, Bureau of Fair Access and Inclusion, the Marrowdale Institute, 418 Penwick Hall, Brackenford, OR 97981-4083, 541-482-6613 (voice), 541-482-6671 (TDD), inclusion@mrwdl.edu.</p></div>
</section>

<section class="page page--lists">
  <div class="masthead-unit">Document Title</div>
  <div class="wordmark masthead-mark">MARROWDALE</div>
  <div class="content">
    <h2 class="section-title">BULLET LIST</h2>
    <ul class="bullets">
      <li><svg width="9" height="9" viewBox="0 0 10 10"><circle cx="5" cy="5" r="5" fill="#fbd400"/><path d="M2.6 5.2 4.3 6.8 7.5 3.4" fill="none" stroke="#000" stroke-width="1.3"/></svg>IPN Bullet 1</li>
      <li class="sub"><svg width="5" height="5" viewBox="0 0 6 6"><circle cx="3" cy="3" r="2.4" fill="none" stroke="#000" stroke-width="0.9"/></svg>IPN Bullet 2</li>
      <li><svg width="9" height="9" viewBox="0 0 10 10"><circle cx="5" cy="5" r="5" fill="#fbd400"/><path d="M2.6 5.2 4.3 6.8 7.5 3.4" fill="none" stroke="#000" stroke-width="1.3"/></svg>IPN Bullet 3</li>
      <li class="sub"><svg width="5" height="5" viewBox="0 0 6 6"><circle cx="3" cy="3" r="2.4" fill="none" stroke="#000" stroke-width="0.9"/></svg>IPN Bullet 4</li>
      <li><svg width="9" height="9" viewBox="0 0 10 10"><circle cx="5" cy="5" r="5" fill="#fbd400"/><path d="M2.6 5.2 4.3 6.8 7.5 3.4" fill="none" stroke="#000" stroke-width="1.3"/></svg>IPN Bullet 5</li>
    </ul>
    <h2 class="section-title" style="margin-top:26px;margin-bottom:0">TABLE 01</h2>
    <table class="data-table table-gold">
      <tr><th>Name</th><th>Name</th><th>Name</th><th>Name</th><th>Name</th></tr>
      <tr><td>000</td><td>000</td><td>000</td><td>000</td><td>000</td></tr>
      <tr><td>000</td><td>000</td><td>000</td><td>000</td><td>000</td></tr>
      <tr><td>000</td><td>000</td><td>000</td><td>000</td><td>000</td></tr>
    </table>
    <p class="caption">Figure 1: Table 1</p>
    <h3 class="table-title-2">TABLE 02</h3>
    <table class="data-table table-black">
      <tr><th>Name</th><th>Name</th><th>Name</th><th>Name</th></tr>
      <tr><td>000</td><td>000</td><td>000</td><td>000</td></tr>
      <tr><td>000</td><td>000</td><td>000</td><td>000</td></tr>
      <tr><td>000</td><td>000</td><td>000</td><td>000</td></tr>
    </table>
    <p class="caption">Figure 2: Table 2</p>
  </div>
  <blockquote class="pull-quote">
    <span class="pull-quote-mark">&ldquo;</span>
    <p>Pellentesque habitant morbi tristique senectus et netus et malesuada fames ac turpis egestas. Proin pharetra nonummy pede. Mauris et orci.</p>
  </blockquote>
  <div class="doc-footer"><p>The Marrowdale Institute prohibits discrimination in employment, educational programs, and activities on the basis of race, creed, color, religion, national origin, age, sex, pregnancy, disability, genetic information, status as a U.S. veteran, service in the U.S. military, sexual orientation, gender identity, associational preferences, or any other classification that deprives the person of consideration as an individual. The university also affirms its commitment to providing equal opportunities and equal access to university facilities. For additional information on nondiscrimination policies, contact the Director, Bureau of Fair Access and Inclusion, the Marrowdale Institute, 418 Penwick Hall, Brackenford, OR 97981-4083, 541-482-6613 (voice), 541-482-6671 (TDD), inclusion@mrwdl.edu.</p></div>
</section>

<section class="page page--contents">
  <div class="masthead-unit">Document Title</div>
  <div class="wordmark masthead-mark">MARROWDALE</div>
  <div class="content" style="top:64px">
    <h2 class="contents-title">CONTENTS</h2>
    <ol class="toc">
      <li class="primary">HEADING 01<span class="leader"></span>3</li>
      <li>HEADING 02<span class="leader"></span>3</li>
      <li class="primary">BULLET LIST<span class="leader"></span>4</li>
      <li class="primary">TABLE 01<span class="leader"></span>4</li>
      <li>TABLE 02<span class="leader"></span>4</li>
    </ol>
  </div>
  <div class="doc-footer"><p>The Marrowdale Institute prohibits discrimination in employment, educational programs, and activities on the basis of race, creed, color, religion, national origin, age, sex, pregnancy, disability, genetic information, status as a U.S. veteran, service in the U.S. military, sexual orientation, gender identity, associational preferences, or any other classification that deprives the person of consideration as an individual. The university also affirms its commitment to providing equal opportunities and equal access to university facilities. For additional information on nondiscrimination policies, contact the Director, Bureau of Fair Access and Inclusion, the Marrowdale Institute, 418 Penwick Hall, Brackenford, OR 97981-4083, 541-482-6613 (voice), 541-482-6671 (TDD), inclusion@mrwdl.edu.</p></div>
</section>

</body>
</html>
```